Technology Project Portal - Project Listing portal

We require a logo & website designed for our new project.

Project Name: lumafold
Description:
We have a webapp where clients and service providers can come, signup and register development projects. Service providers can the browse projects and contact clients via the portal

Design brief:
Clean & Modern - See Attached color palet & style references. (Feel free to try alternative color palets)

See Project Proposal for site requirements.
UX flow section details pages requires

Examples of all standard UI Components required e.g.
text box / field
Drop down
date picker
etc..

Target Market(s)

Business / Technology providers

Logo Text

LumaFold

Coding

Coded - Design and coding required

Number of Pages Required

5+ page

Requirements
Must have
• Clean Modern Design
Examples for all common UI elements
Templates for common Web App Dialogs e.g. Confirm Delete/Logout etc

```html
<!DOCTYPE html>
<html lang="en">
<head>
<meta charset="utf-8">
<title>LumaFold – Login</title>
<link rel="stylesheet" href="https://fonts.googleapis.com/css2?family=Roboto:wght@300;400;500;700&display=swap">
<style>
  :root {
    --coral: #ff8a65;
    --coral-soft: #fb8a70;
    --sage: #8a8f75;
    --blend: #c98d78;
    --white: #ffffff;
    --ink: #1a1a1a;
    --muted: #6e6e6e;
    --placeholder: #a8a8a8;
    --line: #e2e2e2;
    --captcha-bg: #f9f9f9;
    --captcha-line: #d3d3d3;
    --captcha-mark: #7a8d99;
  }
  * { box-sizing: border-box; margin: 0; padding: 0; }
  html, body { width: 1200px; height: 800px; overflow: hidden; }
  body { font-family: "Roboto", Arial, sans-serif; background: var(--white); position: relative; }

  .hero {
    position: absolute; left: 0; top: 0; width: 746px; height: 800px;
    color: var(--white); overflow: hidden;
  }
  .hero-art {
    position: absolute; inset: 0;
    background: linear-gradient(90deg, var(--sage) 0%, var(--blend) 45%, var(--coral) 100%);
  }
  .brand {
    position: absolute; left: 32px; top: 26px;
    font-size: 34px; font-weight: 700; letter-spacing: 0.5px; line-height: 1;
  }
  .hero-title {
    position: absolute; left: 32px; top: 316px;
    font-size: 38px; font-weight: 500; line-height: 47px;
  }
  .hero-text {
    position: absolute; left: 32px; top: 421px; width: 545px;
    font-size: 14.5px; font-weight: 400; line-height: 19px;
  }
  .hero-cta {
    position: absolute; left: 32px; top: 498px; width: 129px; height: 38px;
    background: var(--white); color: var(--coral); border-radius: 19px;
    font-size: 12px; display: flex; align-items: center; justify-content: center;
    text-decoration: none;
  }
  .hero-footer {
    position: absolute; left: 32px; top: 757px; font-size: 11px;
  }

  .login {
    position: absolute; left: 746px; top: 0; width: 454px; height: 800px;
  }
  .greeting { position: absolute; left: 32px; top: 39px; font-size: 11px; color: var(--muted); }
  .close { position: absolute; left: 408px; top: 39px; width: 15px; height: 15px; }
  .login-title {
    position: absolute; left: 0; width: 450px; top: 272px; text-align: center;
    font-size: 24px; font-weight: 400; color: var(--ink);
  }
  .login-sub {
    position: absolute; left: 0; width: 454px; top: 311px; text-align: center;
    font-size: 11.5px; color: var(--muted); font-weight: 300;
  }
  .field {
    position: absolute; left: 67px; width: 320px; height: 38px;
    border: 1px solid var(--line); background: var(--white);
    font: 300 11.5px "Roboto", Arial, sans-serif; color: var(--ink);
    padding: 0 19px; outline: none;
  }
  .field::placeholder { color: var(--placeholder); }
  .field-email { top: 354px; }
  .field-password { top: 408px; }
  .captcha {
    position: absolute; left: 67px; top: 462px; width: 132px; height: 39px;
    background: var(--captcha-bg); border: 1px solid var(--captcha-line); border-radius: 2px;
    display: flex; align-items: center; padding-left: 8px;
  }
  .captcha-box { width: 13px; height: 13px; border: 1px solid #c1c1c1; background: var(--white); border-radius: 2px; }
  .captcha-label { font-size: 7.5px; color: #333; margin-left: 7px; }
  .captcha-mark { position: absolute; right: 8px; top: 9px; width: 20px; height: 20px; border-radius: 50%; background: var(--captcha-mark); }
  .forgot {
    position: absolute; right: 67px; top: 475px; font-size: 10px; color: var(--muted); text-decoration: none;
  }
  .login-btn {
    position: absolute; left: 167px; top: 541px; width: 120px; height: 38px;
    background: var(--coral-soft); color: var(--white); border: 0; border-radius: 19px;
    font: 400 12px "Roboto", Arial, sans-serif;
  }
  .signup-prompt {
    position: absolute; left: 0; width: 454px; top: 738px; text-align: center;
    font-size: 11.5px; color: var(--muted); font-weight: 300;
  }
  .signup-link {
    position: absolute; left: 0; width: 454px; top: 757px; text-align: center;
    font-size: 11.5px; color: var(--coral); text-decoration: none;
  }
</style>
</head>
<body>
  <section class="hero">
    <div class="hero-art" role="img" aria-label="Abstract flowing wave and sphere artwork in sage and coral tones"></div>
    <div class="brand">LumaFold</div>
    <h1 class="hero-title">Lorem ipsum dolor sit amet,<br>consectetur adipiscing</h1>
    <p class="hero-text">ducimus qui blanditiis praesentium voluptatum deleniti atque corrupti quos dolores et quas molestias excepturi sint occaecati cupiditate non provident</p>
    <a class="hero-cta" href="#">Sign Up Today!</a>
    <p class="hero-footer">© 2020 LumaFold</p>
  </section>

  <section class="login">
    <p class="greeting">Welcome Back!</p>
    <svg class="close" viewBox="0 0 15 15" aria-label="Close">
      <path d="M1 1 L14 14 M14 1 L1 14" stroke="#ff8a65" stroke-width="1.5"/>
    </svg>
    <h2 class="login-title">Login Now!</h2>
    <p class="login-sub">Please login to continue using our app</p>
    <input class="field field-email" type="text" placeholder="Name@email.com">
    <input class="field field-password" type="password" placeholder="Password">
    <div class="captcha">
      <span class="captcha-box"></span>
      <span class="captcha-label">I'm not a robot</span>
      <span class="captcha-mark"></span>
    </div>
    <a class="forgot" href="#">Forgot Password?</a>
    <button class="login-btn">Login</button>
    <p class="signup-prompt">Don't have an account?</p>
    <a class="signup-link" href="#">Sign Up</a>
  </section>
</body>
</html>
```